Bramblecart Store > Into Website

Hello - this is our Bramblecart Store
https://www.bramblecart.example/stores/KELVORANEST/page/7D4810A2-B31F-42CE-91D3-AACE772810FD?ref_=qz_mrk
I need someone to use the text from out listings, he details, and description PLUS the images here and create a very simple but modern website designed as a brochure / shopping / feature site.

All [Add to Cart] buttons will jump to Bramblecart, so this site is designed as a web presence for the Bramblecart store.

Domain will be www.KelvoraNest.example

Nav Link:
About Setup Instructions Tutorials FAQ Contact

Ideal candidate will have experience working with ecommerce, and working with detailed listings. All the details on the Bramblecart listings page are important (size / weight /etc) so it's a challenge to make all this readable and friendly.

Please be ready to start immediately and ready to delivery code-ready Figma files within a week.

```html
<!DOCTYPE html>
<html lang="en">
<head>
<meta charset="UTF-8">
<title>Aerial Sling Ceiling Hooks</title>
<link rel="stylesheet" href="https://fonts.googleapis.com/css2?family=Open+Sans:wght@400;700&display=swap">
<style>
  :root {
    --brand-violet: #624bff;
    --photo-lavender: #b3afcf;
    --photo-lavender-deep: #a49fc6;
    --text-white: #ffffff;
    --cta-amber: #fdb022;
  }
  * { box-sizing: border-box; margin: 0; padding: 0; }
  html, body {
    width: 1200px;
    height: 611px;
    overflow: hidden;
  }
  body {
    font-family: "Open Sans", Arial, sans-serif;
    background: var(--brand-violet);
  }
  .product-slide {
    position: relative;
    width: 1200px;
    height: 611px;
    display: flex;
  }
  .product-media {
    width: 600px;
    height: 611px;
    background: radial-gradient(ellipse at 50% 45%, var(--photo-lavender) 55%, var(--photo-lavender-deep) 100%);
  }
  .product-info {
    position: relative;
    width: 600px;
    height: 611px;
    background: var(--brand-violet);
    color: var(--text-white);
  }
  .section-eyebrow {
    position: absolute;
    left: 70px;
    top: 77px;
    font-size: 16px;
    font-weight: 700;
    letter-spacing: 0.2px;
    text-transform: uppercase;
  }
  .product-title {
    position: absolute;
    left: 70px;
    top: 110px;
    font-size: 32px;
    font-weight: 700;
    line-height: 44px;
    white-space: nowrap;
  }
  .product-description {
    position: absolute;
    left: 70px;
    top: 193px;
    width: 425px;
    font-size: 14px;
    font-weight: 400;
    line-height: 25px;
  }
  .add-to-cart {
    position: absolute;
    left: 70px;
    top: 309px;
    width: 160px;
    height: 48px;
    display: flex;
    align-items: center;
    justify-content: center;
    background: var(--cta-amber);
    color: var(--text-white);
    font-size: 16px;
    font-weight: 700;
    text-decoration: none;
    border-radius: 4px;
  }
  .slide-dots {
    position: absolute;
    left: 70px;
    top: 520px;
    display: flex;
    align-items: center;
  }
  .slide-dot {
    width: 10px;
    height: 10px;
    border-radius: 50%;
    background: var(--text-white);
    margin-right: 18px;
  }
  .slide-dot--active {
    width: 21px;
    height: 21px;
    background: transparent;
    border: 4px solid var(--text-white);
    margin-right: 13px;
    margin-left: -5px;
  }
</style>
</head>
<body>
  <main class="product-slide">
    <div class="product-media" role="img" aria-label="Two grey round ceiling hook plates with crossed loops, shown with their anchor bolts and screws"></div>
    <section class="product-info">
      <p class="section-eyebrow">Our Products</p>
      <h1 class="product-title">Aerial Sling Ceiling Hooks</h1>
      <p class="product-description">Our iron clad yet minimalistic Ceiling Hooks allow you to hang your Aerial Sling in any room of the house. It;s perfect for indoor or outdoor setup in wood or concrete beams.</p>
      <a class="add-to-cart" href="https://www.bramblecart.example/stores/KELVORANEST/page/7D4810A2-B31F-42CE-91D3-AACE772810FD?ref_=qz_mrk">Add to Cart</a>
      <div class="slide-dots" aria-label="Slide 3 of 4">
        <span class="slide-dot"></span>
        <span class="slide-dot"></span>
        <span class="slide-dot slide-dot--active"></span>
        <span class="slide-dot"></span>
      </div>
    </section>
  </main>
</body>
</html>
```